Brochure about Gun Trusts

Cover Page: Image of a firearm collection or a lockbox with the title]
Headline: Protect Your Firearms Collection with a Gun Trust
Subheading: Ensure Your Legacy Remains Private and Your Wishes Are Respected
[Page 1: What is a Gun Trust?]
Definition: A legally recognized trust that allows you to collect, own, and transfer firearms, including those restricted by the NFA.
Quote: "A gun trust is a revocable trust created to hold ownership of a firearm..." - QMR
[Page 2: Benefits of a Gun Trust]
Avoid Probate: Keep your firearms out of the public probate process, maintaining your privacy.
Multi-Generational Ownership: Easily transfer ownership to beneficiaries without the need for a court proceeding.
Shared Responsibility: Allow others to legally possess and use the firearms held in the trust.
[Page 3: The Risks of Not Having a Gun Trust]
Inheritance Issues: Firearms may not be transferred as intended, potentially leading to legal complications.
Probate and Public Disclosure: Your firearms collection becomes a public record.
[Page 4: How to Set Up a Gun Trust]
Consult with an Attorney: A firearms trust attorney will create a trust that complies with all federal and state laws.
Assign a Trustee: Choose a trustee to manage the trust if you become incapacitated or pass away.
Transfer Ownership: Assign your firearms to the trust.
[Back Cover: Call to Action]
Headline: Protect Your Firearms Legacy
Contact Information: Address, Phone Number, Email, Website
Offer: Free Consultation to discuss your options

```html
<!DOCTYPE html>
<html lang="en">
<head>
<meta charset="utf-8">
<title>Gun Trust Brochure</title>
<link href="https://fonts.googleapis.com/css2?family=Montserrat:wght@500;600;700;800;900&family=Poppins:wght@400;500;600&display=swap" rel="stylesheet">
<style>
:root{
  --paper:#ffffff;
  --ink-dark:#141110;
  --ink-brown:#2a1f18;
  --wood:#5a3a22;
  --gold:#b8924f;
  --gold-light:#d3ad6a;
  --text:#f3eee6;
  --muted:#b9ada0;
}
*{margin:0;padding:0;box-sizing:border-box}
html,body{width:1200px;height:2180px;overflow:hidden;background:var(--paper)}
.canvas{position:relative;width:1200px;height:2180px}
.page{position:absolute;width:500px;height:662px;overflow:hidden;background:var(--ink-dark);color:var(--text);font-family:'Poppins',sans-serif}
.col-a{left:82px}.col-b{left:618px}
.row-1{top:60px}.row-2{top:759px}.row-3{top:1458px}
.photo{position:absolute}
.kicker{font-family:'Montserrat',sans-serif;font-weight:600;letter-spacing:4px;font-size:15px;text-transform:uppercase}
.display{font-family:'Montserrat',sans-serif;font-weight:900;text-transform:uppercase;line-height:.92}
.gold{color:var(--gold)}
.url{position:absolute;left:34px;bottom:20px;font-size:11px;color:var(--muted);letter-spacing:1px}
.tag{position:absolute;right:24px;bottom:18px;width:46px;height:16px;background:var(--gold)}
.small{font-size:11px;line-height:1.45;color:var(--muted)}
</style>
</head>
<body>
<div class="canvas">

<!-- Cover -->
<section class="page col-a row-1 cover">
  <div class="photo" role="img" aria-label="Open wooden lockbox holding a pistol and ammunition" style="left:0;top:250px;width:500px;height:412px;background:radial-gradient(ellipse at 50% 45%,#6b4a30 0%,#3a271a 45%,#141110 90%)"></div>
  <div style="position:absolute;left:34px;top:40px">
    <p class="kicker gold">Protect your</p>
    <p class="display" style="font-size:34px;margin-top:8px;line-height:1.05">Firearms<br>Collection <span style="font-size:20px;text-transform:none;font-weight:600">with a</span></p>
    <p class="display gold" style="font-size:72px;margin-top:8px">Gun</p>
    <p class="display" style="font-size:72px">Trust</p>
    <p class="small" style="margin-top:14px;width:250px">Ensure Your Legacy Remains Private and Your Wishes Are Respected</p>
  </div>
  <p class="url">www.trustvault-legal.com</p>
</section>

<!-- What is -->
<section class="page col-b row-1 what">
  <div class="photo" role="img" aria-label="Black rifle resting on a dark surface" style="left:0;top:250px;width:500px;height:412px;background:linear-gradient(160deg,#2b2520 0%,#1a1613 55%,#0e0c0b 100%)"></div>
  <div style="position:absolute;left:34px;top:40px">
    <p class="kicker" style="color:var(--text)">What is a</p>
    <p class="display gold" style="font-size:60px;margin-top:8px">Gun</p>
    <p class="display gold" style="font-size:60px">Trust?</p>
    <div style="width:200px;margin-top:18px;background:var(--gold);padding:10px 12px;font-size:11px;line-height:1.45;color:var(--ink-dark)">A legally recognized trust that allows you to collect, own, and transfer firearms, including those restricted by the NFA.</div>
  </div>
  <div style="position:absolute;left:290px;top:40px;width:180px">
    <p class="display" style="font-size:90px;color:#3c332c;line-height:.7">&ldquo;</p>
    <p class="small" style="margin-top:12px">A gun trust is a revocable trust created to hold ownership of a firearm...</p>
    <p class="small gold" style="margin-top:6px">- QMR</p>
  </div>
  <div class="tag"></div>
  <p class="url">www.trustvault-legal.com</p>
</section>

<!-- Benefits -->
<section class="page col-a row-2 benefits">
  <div class="photo" role="img" aria-label="Hand aiming a pistol at an outdoor range" style="left:0;top:380px;width:500px;height:282px;background:linear-gradient(180deg,#8a7e62 0%,#6c5f45 50%,#3b3426 100%)"></div>
  <div style="position:absolute;left:34px;top:38px">
    <p class="kicker" style="color:var(--text)">Benefits of a</p>
    <p class="display gold" style="font-size:54px;margin-top:8px">Gun</p>
    <p class="display" style="font-size:54px">Trust</p>
  </div>
  <div style="position:absolute;left:34px;top:205px;width:432px;display:flex;gap:8px">
    <div style="flex:1;background:var(--gold);padding:10px;color:var(--ink-dark)">
      <p style="font-family:'Montserrat',sans-serif;font-weight:800;font-size:11px;text-transform:uppercase;text-align:center">Avoid Probate</p>
      <p style="font-size:9px;line-height:1.4;margin-top:6px;text-align:center">Keep your firearms out of the public probate process, maintaining your privacy.</p>
    </div>
    <div style="flex:1;background:var(--gold);padding:10px;color:var(--ink-dark)">
      <p style="font-family:'Montserrat',sans-serif;font-weight:800;font-size:11px;text-transform:uppercase;text-align:center">Multi-Generational Ownership</p>
      <p style="font-size:9px;line-height:1.4;margin-top:6px;text-align:center">Easily transfer ownership to beneficiaries without a court proceeding.</p>
    </div>
    <div style="flex:1;background:var(--gold);padding:10px;color:var(--ink-dark)">
      <p style="font-family:'Montserrat',sans-serif;font-weight:800;font-size:11px;text-transform:uppercase;text-align:center">Shared Responsibility</p>
      <p style="font-size:9px;line-height:1.4;margin-top:6px;text-align:center">Allow others to legally possess and use the firearms held in the trust.</p>
    </div>
  </div>
  <p class="url">www.trustvault-legal.com</p>
</section>

<!-- Risks -->
<section class="page col-b row-2 risks">
  <div class="photo" role="img" aria-label="Rifles and a pistol laid out on a wooden table" style="left:0;top:330px;width:500px;height:332px;background:linear-gradient(180deg,#2a221c 0%,#4a3626 60%,#2a1d14 100%)"></div>
  <div style="position:absolute;left:34px;top:40px">
    <p class="kicker" style="color:var(--text)">The risks of</p>
    <p class="display" style="font-size:30px;margin-top:10px;background:var(--gold);color:var(--ink-dark);padding:6px 10px;display:inline-block">Not having a</p>
    <p class="display" style="font-size:58px;margin-top:12px">Gun</p>
    <p class="display gold" style="font-size:58px">Trust</p>
  </div>
  <div style="position:absolute;left:292px;top:40px;width:178px">
    <div style="border:1px solid var(--gold);padding:10px">
      <p style="font-family:'Montserrat',sans-serif;font-weight:800;font-size:11px;text-transform:uppercase" class="gold">Inheritance Issues</p>
      <p class="small" style="font-size:9px;margin-top:4px">Firearms may not be transferred as intended, potentially leading to legal complications.</p>
    </div>
    <div style="border:1px solid var(--gold);padding:10px;margin-top:10px">
      <p style="font-family:'Montserrat',sans-serif;font-weight:800;font-size:11px;text-transform:uppercase" class="gold">Probate and Public Disclosure</p>
      <p class="small" style="font-size:9px;margin-top:4px">Your firearms collection becomes a public record.</p>
    </div>
  </div>
  <div class="tag"></div>
  <p class="url">www.trustvault-legal.com</p>
</section>

<!-- How to -->
<section class="page col-a row-3 howto">
  <div class="photo" role="img" aria-label="Close view of a handgun in dim light" style="left:250px;top:0;width:250px;height:260px;background:linear-gradient(135deg,#3a2f27 0%,#1b1714 100%)"></div>
  <div class="photo" role="img" aria-label="Single cartridge standing on a dark table" style="left:250px;top:260px;width:250px;height:402px;background:radial-gradient(ellipse at 40% 60%,#6a4a2c 0%,#2a1e16 55%,#141110 100%)"></div>
  <div style="position:absolute;left:34px;top:40px">
    <p class="kicker" style="color:var(--text)">How to set up a</p>
    <p class="display gold" style="font-size:54px;margin-top:8px">Gun</p>
    <p class="display" style="font-size:54px">Trust</p>
  </div>
  <div style="position:absolute;left:0;top:250px;width:250px;height:330px;background:var(--gold);padding:24px 20px 0 34px;color:var(--ink-dark)">
    <p style="font-family:'Montserrat',sans-serif;font-weight:800;font-size:12px;text-transform:uppercase">01 Consult with an Attorney</p>
    <p style="font-size:10px;line-height:1.4;margin-top:4px">A firearms trust attorney will create a trust that complies with all federal and state laws.</p>
    <p style="font-family:'Montserrat',sans-serif;font-weight:800;font-size:12px;text-transform:uppercase;margin-top:18px">02 Assign a Trustee</p>
    <p style="font-size:10px;line-height:1.4;margin-top:4px">Choose a trustee to manage the trust if you become incapacitated or pass away.</p>
    <p style="font-family:'Montserrat',sans-serif;font-weight:800;font-size:12px;text-transform:uppercase;margin-top:18px">03 Transfer Ownership</p>
    <p style="font-size:10px;line-height:1.4;margin-top:4px">Assign your firearms to the trust.</p>
  </div>
  <p class="url">www.trustvault-legal.com</p>
</section>

<!-- Back cover -->
<section class="page col-b row-3 back">
  <div class="photo" role="img" aria-label="Hand reaching for a pistol on a wooden table" style="left:0;top:0;width:500px;height:662px;background:linear-gradient(170deg,#6a4a2e 0%,#4a321f 40%,#1e1712 75%,#141110 100%)"></div>
  <div style="position:absolute;left:0;right:0;top:430px;text-align:center">
    <p class="kicker gold" style="font-size:13px">Protect your</p>
    <p class="display" style="font-size:30px;margin-top:6px">Firearms<br>Collection</p>
    <p style="display:inline-block;margin-top:12px;background:var(--gold);color:var(--ink-dark);font-size:10px;padding:5px 14px;font-weight:600">Free Consultation to discuss your options</p>
    <p class="small" style="margin-top:12px;font-size:10px">(555) 014-2290</p>
    <p class="small" style="font-size:10px">410 Oak Ridge Lane, Suite 2</p>
    <p class="small" style="font-size:10px">hello@trustvault-legal.com</p>
    <p class="small" style="font-size:10px;margin-top:10px">www.trustvault-legal.com</p>
  </div>
</section>

</div>
</body>
</html>
```